Menu revision for Korean Restaurant

I have posted the exact content in a word file that I would like to appear in the menu. Please apply to the template. I will be following up with prices shortly. I am in a hurry and not too picky. Thank you.

Make a menu with revisions.

Page 1: Cover Page
- Replace logo with new uploaded logo

Page 2:
Appetizers
Vegetarian Appetizers

Page 3:
BBQ Items

Page 4:
Signature Dishes

Page 5:
Bokkeum | Stir-Fry

Page 6:
Rice Bowls
Noodles
Hot Soup

Page 7:
Drinks

Target Market(s)

My customers

Industry/Entity Type

Restaurant

Requirements
Must have
• 1. Only use my menu content, template, and font.

```html
<!DOCTYPE html>
<html lang="en">
<head>
<meta charset="UTF-8">
<title>Bokkeum | Stir-Fry</title>
<link href="https://fonts.googleapis.com/css2?family=Barlow+Semi+Condensed:wght@700&family=Barlow:wght@700&family=Merriweather:wght@400&family=Nanum+Myeongjo:wght@400&display=swap" rel="stylesheet">
<style>
  :root {
    --page-bg: #333333;
    --frame-gold: #b39a62;
    --name-gold: #c8ab6e;
    --title-red: #c4353b;
    --body-text: #f2f0ea;
  }
  * { margin: 0; padding: 0; box-sizing: border-box; }
  html, body { width: 928px; height: 1200px; overflow: hidden; background: var(--page-bg); }
  .menu-page { position: relative; width: 928px; height: 1200px; background: var(--page-bg); }
  .page-frame { position: absolute; inset: 0; }
  .section-title {
    position: absolute; top: 40px; left: 0; width: 100%;
    text-align: center;
    font-family: "Barlow Semi Condensed", "Arial Narrow", sans-serif;
    font-weight: 700; font-size: 56px; letter-spacing: 2px;
    color: var(--title-red); line-height: 1;
  }
  .dish-column { position: absolute; top: 131px; width: 392px; }
  .dish-column.left { left: 59px; }
  .dish-column.right { left: 479px; }
  .dish {
    font-family: "Merriweather", Georgia, serif;
    font-size: 13.5px; line-height: 19.5px; color: var(--body-text);
    text-align: justify; margin-bottom: 22px;
  }
  .dish-name {
    font-family: "Barlow", Arial, sans-serif; font-weight: 700;
    font-size: 14px; color: var(--name-gold); letter-spacing: 0.3px;
  }
  .dish-korean {
    font-family: "Nanum Myeongjo", serif; font-size: 13px; color: var(--name-gold);
  }
  .divider { position: absolute; top: 418px; left: 254px; width: 420px; height: 46px; }
  .divider-line { position: absolute; top: 22px; height: 1px; width: 162px; background: var(--frame-gold); }
  .divider-line.left { left: 0; }
  .divider-line.right { right: 0; }
  .divider-medallion {
    position: absolute; left: 187px; top: 0; width: 46px; height: 46px; border-radius: 50%;
    background: radial-gradient(circle, #5a5040 0%, #3d382f 70%);
    border: 1.5px solid var(--frame-gold);
  }
</style>
</head>
<body>
<main class="menu-page">
  <svg class="page-frame" width="928" height="1200" viewBox="0 0 928 1200" aria-hidden="true">
    <g fill="none" stroke="#b39a62" stroke-width="1.5">
      <rect x="48" y="48" width="832" height="1104"/>
      <rect x="30" y="30" width="34" height="34"/>
      <rect x="864" y="30" width="34" height="34"/>
      <rect x="30" y="1136" width="34" height="34"/>
      <rect x="864" y="1136" width="34" height="34"/>
      <rect x="38" y="38" width="18" height="18"/>
      <rect x="872" y="38" width="18" height="18"/>
      <rect x="38" y="1144" width="18" height="18"/>
      <rect x="872" y="1144" width="18" height="18"/>
    </g>
  </svg>

  <h1 class="section-title">BOKKEUM | STIR-FRY</h1>

  <section class="dish-column left">
    <p class="dish"><span class="dish-name">Jeyuk Bokkeum</span> <span class="dish-korean">제육볶음</span> Pork, onions, scallions, mushrooms and jalapenos stir-fried in a spicy red garlic sauce</p>
    <p class="dish"><span class="dish-name">Dubu Bokkeum (v)</span> <span class="dish-korean">두부볶음</span> Fried tofu cubes, zucchini, carrots, onions, and mushrooms stir-fried in a red chili sauce</p>
    <p class="dish"><span class="dish-name">Kimchi Bokkeum</span> <span class="dish-korean">김치볶음</span> Pork, kimchi, rice cakes, scallions, onions, and fresh tofu</p>
    <p class="dish"><span class="dish-name">Haemul Bokkeum</span> <span class="dish-korean">해물볶음</span> Jumbo shrimp, scallops, mussels, calamari, octopus, zucchini, carrots, onions, scallions, mushrooms, and jalapenos</p>
  </section>

  <section class="dish-column right">
    <p class="dish"><span class="dish-name">Samgyupsal Bokkeum</span> <span class="dish-korean">매운삼겹살</span> Pork belly, zucchini, onions, scallions stir-fried in a spicy gochu wine sauce</p>
    <p class="dish"><span class="dish-name">Ojingeo Bokkeum</span> <span class="dish-korean">오징어볶음</span> Fresh calamari stir-fried with carrots, zucchini, mushrooms, onions and scallions in a hot and spicy chili sauce</p>
    <p class="dish"><span class="dish-name">Nakji Bokkeum</span> <span class="dish-korean">낙지볶음</span> Fresh ctopus stir-fried with carrots, zucchini, mushrooms, onions, and scallions in a hot and spicy chili sauce</p>
    <p class="dish"><span class="dish-name">Jjuggumi Samgyupsal</span> <span class="dish-korean">쭈꾸미삼겹살</span> Spicy pork belly and baby octopus</p>
  </section>

  <div class="divider">
    <span class="divider-line left"></span>
    <div class="divider-medallion" role="img" aria-label="Round ornamental medallion"></div>
    <span class="divider-line right"></span>
  </div>
</main>
</body>
</html>
```